Investment Company Business Card Design

We need a Business Card design for a new company based in Boston called "Velm Investment". We are cooperating with local real estate and construction companies. Our company is very actively and aggressively acquiring primarily residential investment properties either to buy and hold long term or for purposes or renovating and repositioning for re-sale in the market. In addition, we undertake some development projects and acquisitions as opportunities present themselves. the final design should contains information about “Velm" the river boat. we are tenacious, indomitable, and the business have a favorable wind throughout the voyage for all our investment.
sample Info. on Design:
Tusa Merrick
CEO
555-xxx-xxxx
418 Harlow St. Suite 507, Alderbrook, MA 01987
Please provide a template also, that we can edit the info later.
Reason: i just got new LOGO Design attached will be use in Business Card Design.
Construction

```html
<!DOCTYPE html>
<html lang="en">
<head>
<meta charset="utf-8">
<title>Velm Investment – Business Card</title>
<link href="https://fonts.googleapis.com/css2?family=Montserrat:wght@300;400&display=swap" rel="stylesheet">
<style>
  :root {
    --page: #ffffff;
    --card-outline: #3a3a3a;
    --card-dark: #000000;
    --gold: #c9a24a;
    --silver: #9a9a9a;
    --ink: #111111;
    --ink-soft: #555555;
    --rule: #777777;
  }
  html, body {
    margin: 0;
    padding: 0;
    width: 1200px;
    height: 967px;
    overflow: hidden;
    background: var(--page);
    font-family: "Montserrat", sans-serif;
  }
  .canvas {
    position: relative;
    width: 1200px;
    height: 967px;
  }
  .card-front {
    position: absolute;
    left: 89px;
    top: 145px;
    width: 359px;
    height: 645px;
    box-sizing: border-box;
    border: 1px solid var(--card-outline);
    border-radius: 180px;
    background: var(--page);
  }
  .card-back {
    position: absolute;
    left: 513px;
    top: 287px;
    width: 644px;
    height: 360px;
    border-radius: 180px;
    background: var(--card-dark);
  }
  .brand {
    position: absolute;
    line-height: 1;
  }
  .brand-name {
    color: var(--gold);
    font-weight: 400;
    letter-spacing: 0.04em;
    text-transform: uppercase;
    white-space: nowrap;
  }
  .brand-tagline {
    color: var(--silver);
    font-weight: 300;
    text-transform: uppercase;
    letter-spacing: 0.06em;
    white-space: nowrap;
  }
  .card-front .brand {
    left: 48px;
    top: 130px;
  }
  .card-front .brand-name { font-size: 26px; }
  .card-front .brand-tagline { font-size: 8px; margin-top: 6px; }
  .card-back .brand {
    left: 140px;
    top: 170px;
  }
  .card-back .brand-name { font-size: 40px; }
  .card-back .brand-tagline { font-size: 11px; margin-top: 8px; }
  .divider {
    position: absolute;
    left: 90px;
    top: 411px;
    width: 179px;
    height: 5px;
    box-sizing: border-box;
    border-top: 1px solid var(--rule);
    border-bottom: 1px solid var(--rule);
  }
  .contact {
    position: absolute;
    left: 0;
    right: 0;
    top: 430px;
    text-align: center;
    color: var(--ink-soft);
    font-weight: 300;
  }
  .contact p { margin: 0; }
  .contact .role { font-size: 15px; line-height: 20px; }
  .contact .person {
    font-size: 24px;
    line-height: 32px;
    color: var(--ink);
    font-weight: 400;
    letter-spacing: 0.02em;
  }
  .contact .line { font-size: 17px; line-height: 28px; letter-spacing: 0.02em; }
</style>
</head>
<body>
<main class="canvas">
  <section class="card-front">
    <div class="brand">
      <div class="brand-name">Velm Invest</div>
      <div class="brand-tagline">Property Investment &amp; Development</div>
    </div>
    <div class="divider"></div>
    <div class="contact">
      <p class="role">CEO</p>
      <p class="person">TUSA MERRICK</p>
      <p class="line">555.xxx.xxxx</p>
      <p class="line">418 Harlow St. Suite 507,</p>
      <p class="line">Alderbrook, MA 01987</p>
    </div>
  </section>
  <section class="card-back">
    <div class="brand">
      <div class="brand-name">Velm Invest</div>
      <div class="brand-tagline">Property Investment &amp; Development</div>
    </div>
  </section>
</main>
</body>
</html>
```